Neue Website fuer Software-Firma (CMS: Joomla, Responsive Design)
Zielgruppe
Die VANTRIX ist ein Software- und Beratungshaus im Lager- und Produktionslogistikbereich. Unsere Kunden sind Industriefirmen und Logistikdienstleister, die ein oder mehrere Laeger bewirtschaften und dafuer eine Software und mobile Datenerfassung einsetzen. Fast alle unserer Kunden haben KVT im Einsatz.
Aufgabenstellung
Unsere aktuelle Website wurde seit langem nicht mehr gepflegt und ist veraltet.
Wir moechten die neue Website gern mit dem CMS Joomla betreiben (ggf. waere auch Wordpress moeglich). Gern koennen Sie als Basis ein bereits existierendes (freies) Theme verwenden, wenn es entweder bereits alle Ansprueche erfuellt oder Sie es entsprechend anpassen.
Die neue Website soll in jedem Fall responsive sein, d.h. sowohl auf Desktop, Tablet und Smartphone funktionieren und das Design entsprechend anpassen.
Unsere aktuelle Seite steht unter www.vantrix-lagerwerk.example
Eine Seite, die uns besonders gut gefaellt, ist www.quendal.example (die sich auch teilweise an die gleichen Kunden richtet).
Wir moechten ein klares Design. Ein Beispiel, wie eines unserer Dashboards unserer Software aussieht, finden Sie anbei. Die Farbgestaltung darin wird jedoch noch geaendert. Sie wird eher in Richtung der Farbgestaltung der Quendal-Website gehen, jedoch immer noch grundsaetzlich hell sein. Evtl. koennen Sie Elemente daraus aufgreifen? Es soll in jedem Fall ersichtlich sein, dass Website und Software von der gleichen Firma sind.
Es soll moeglichst viel mit Grafiken gearbeitet werden – aehnlich der Quendal-Seite unter der Dia-Show. Diese muessen aber nicht zwingend farbig sein. Ein Mockup fuer einfarbige Grafiken unterhalb einer Diashow habe ich hier erstellt: https://helgard07.seitenbau.example/meinewebsite-1 Bitte orientieren Sie sich aber nicht an dieser Seite selbst – das war nur ein Probierbeispiel.
Desweiteren soll die Seite suchmaschinenfreundlich sein.
In Ihren Leistungen enthalten sein soll:
- Erstellung der Homepage incl.
o Menu (wie bei Quendal soll es ausklappbar sein und mind. 2 Ebenen koennen)
o Login-Button der einen externen Link aufruft
o Auswahl der Sprache (und damit Verlinkung zu jeweils der Homepage in der
ausgewaehlten Sprache
o Moeglichkeit zum Chat
o Suchfeld zum Durchsuchen aller S..

```html
<!DOCTYPE html>
<html lang="en">
<head>
<meta charset="utf-8">
<title>VANTRIX – Software Solutions for Logistics</title>
<link href="https://fonts.googleapis.com/css2?family=Lato:ital,wght@0,300;0,400;0,700;1,300&display=swap" rel="stylesheet">
<style>
:root{
  --red:#cc0000;
  --blue:#0a3697;
  --dark:#16202e;
  --light:#f0f3f6;
  --panel:#e8ecef;
  --panel2:#f1f3f5;
  --text:#2b3240;
  --muted:#7c8591;
  --line:#dde2e7;
}
*{margin:0;padding:0;box-sizing:border-box}
html,body{width:1019px;height:1200px;overflow:hidden;background:#fff}
body{position:relative;font-family:'Lato',sans-serif;color:var(--text);font-size:8px}
.abs{position:absolute}
a{color:inherit;text-decoration:none}

/* header */
.header{left:0;top:0;width:1019px;height:47px;background:var(--light);border-bottom:1px solid var(--red)}
.brand{left:206px;top:13px}
.brand-name{font-weight:400;font-size:18px;color:var(--dark);letter-spacing:1px;line-height:18px}
.brand-tag{font-weight:300;font-size:5.5px;color:var(--muted);letter-spacing:.3px;margin-top:2px}
.menu-btn{left:310px;top:0;width:77px;height:47px;background:var(--panel);display:flex;align-items:center;gap:8px;padding-left:12px;color:var(--red);font-size:10px}
.util{top:16px;display:flex;align-items:center;gap:5px;font-size:8.5px;color:var(--text)}
.social{display:flex;gap:2px}
.social span{width:16px;height:16px;display:block}

/* dropdown */
.drop-main{left:310px;top:47px;width:88px;height:112px;background:var(--panel);padding:7px 8px;z-index:3}
.drop-sub{left:398px;top:47px;width:120px;height:112px;background:var(--panel2);padding:12px 9px;z-index:3;box-shadow:-4px 0 6px rgba(0,0,0,.06)}
.drop-main li,.drop-sub li{list-style:none;font-size:8.3px;line-height:16px;color:var(--dark)}
.drop-main li.on,.drop-sub li.on{color:var(--red)}

/* hero */
.hero{left:0;top:47px;width:1019px;height:333px;background:linear-gradient(90deg,#0f3a9a 0%,#274aa0 40%,#6d7fa8 62%,#a7adb8 80%,#c7c3c0 100%)}
.hero-title{left:236px;top:160px;font-weight:300;font-size:29px;line-height:32px;color:#fff}
.btn-red{left:239px;top:246px;width:138px;height:26px;background:var(--red);color:#fff;font-size:12.5px;display:flex;align-items:center;justify-content:center;letter-spacing:.3px}
.dots{left:494px;top:336px;display:flex;gap:4px}
.dots i{width:5px;height:5px;border-radius:50%;background:rgba(255,255,255,.6);display:block}
.dots i:first-child{background:#fff}

/* tiles */
.tiles-frame{left:198px;top:350px;width:621px;height:106px;background:#fff}
.tiles{left:206px;top:357px;width:606px;height:91px;display:flex;gap:1px}
.tile{flex:1;background:var(--dark);color:#fff;display:flex;flex-direction:column;align-items:center;justify-content:center;gap:8px;font-size:8.5px;letter-spacing:.3px}
.tile.active{background:var(--red)}

/* service cards */
.card{top:489px;width:190px;height:191px;overflow:hidden}
.card-caption{position:absolute;left:12px;bottom:8px;color:#fff;font-size:14.5px;line-height:17px}

/* about / clients */
.h2{font-weight:300;font-size:20px;color:var(--blue)}
.about-lead{left:214px;top:758px;font-style:italic;font-weight:300;font-size:10px;line-height:13px;color:var(--muted)}
.about-body{left:214px;top:799px;width:235px;font-weight:300;font-size:8px;line-height:10.3px;color:var(--text)}
.more{font-size:8.3px;color:var(--blue);display:flex;align-items:center;gap:5px}
.more i{width:3.5px;height:3.5px;background:var(--red);display:block}
.clients{left:466px;top:760px;width:346px;height:108px;display:grid;grid-template-columns:repeat(3,1fr);border:1px solid var(--line)}
.client{display:flex;align-items:center;justify-content:center;gap:4px;border-right:1px solid var(--line);border-bottom:1px solid var(--line);font-size:12px;color:#9aa1aa;letter-spacing:.5px}
.client:nth-child(3n){border-right:0}
.client:nth-child(n+4){border-bottom:0}
.client.focus{background:#fff;box-shadow:0 2px 6px rgba(0,0,0,.12);color:var(--red)}
.client b{width:6px;height:6px;border-radius:50%;background:currentColor;display:block}

/* band */
.band{left:0;top:929px;width:1019px;height:82px;background:var(--blue)}
.band-text{left:215px;top:960px;color:#fff;font-weight:300;font-size:19px}
.btn-outline{left:655px;top:960px;width:156px;height:27px;border:1px solid #fff;color:#fff;font-size:10.5px;display:flex;align-items:center;justify-content:center}

/* footer */
.footer{left:0;top:1011px;width:1019px;height:157px;background:var(--light)}
.fcol{top:1039px}
.fcol h4{font-weight:400;font-size:8.3px;color:var(--red);margin-bottom:10px}
.fcol p,.fcol li{list-style:none;font-weight:300;font-size:8px;line-height:12.7px;color:var(--text);padding-left:2px}
.fcol .mail{color:var(--red)}
.legal{top:1172px;font-weight:300;font-size:8px;color:var(--muted)}

/* chat */
.chat{left:971px;top:598px;width:48px;height:48px;background:var(--red);display:flex;align-items:center;justify-content:center}
</style>
</head>
<body>

<header class="abs header">
  <div class="abs brand">
    <div class="brand-name">VANTRIX</div>
    <div class="brand-tag">Software Solutions For Logistics</div>
  </div>
  <div class="abs menu-btn">
    <svg width="21" height="15" viewBox="0 0 21 15"><rect y="0" width="21" height="2.4" fill="#cc0000"/><rect y="6.2" width="21" height="2.4" fill="#cc0000"/><rect y="12.4" width="21" height="2.4" fill="#cc0000"/></svg>
    Menu
  </div>
  <div class="abs util" style="left:604px">
    <svg width="13" height="14" viewBox="0 0 13 14" fill="none" stroke="#5a6270" stroke-width=".9"><circle cx="6.5" cy="4.2" r="3.4"/><path d="M.6 13.5c.6-3.4 3-5 5.9-5s5.3 1.6 5.9 5z"/></svg>
    Login
  </div>
  <div class="abs util" style="left:673px">
    <svg width="14" height="14" viewBox="0 0 14 14" fill="none" stroke="#5a6270" stroke-width=".9"><circle cx="7" cy="7" r="6.3"/><path d="M.7 7h12.6M7 .7c-2.4 2.5-2.4 10.1 0 12.6M7 .7c2.4 2.5 2.4 10.1 0 12.6"/></svg>
    English
  </div>
  <div class="abs social" style="left:768px;top:16px" aria-label="Social links">
    <span style="background:#3b5a9a"></span><span style="background:#3fa6df"></span><span style="background:#d44132"></span>
  </div>
</header>

<ul class="abs drop-main">
  <li>About us</li><li class="on">Services</li><li>Clients</li><li>News</li><li>Contact</li>
</ul>
<ul class="abs drop-sub">
  <li>KVT Development</li><li>Warehouse Managemen</li><li class="on">Automation / Integration</li><li>Development</li><li>Maintance</li>
</ul>

<section class="abs hero" role="img" aria-label="Warehouse worker scanning parcels between high shelves, blue tint on the left"></section>
<h1 class="abs hero-title">We are conectiong dots in<br>your logistic business</h1>
<a class="abs btn-red">CONTACT US</a>
<div class="abs dots"><i></i><i></i><i></i><i></i></div>

<div class="abs tiles-frame"></div>
<nav class="abs tiles">
  <div class="tile active">
    <svg width="22" height="20" viewBox="0 0 22 20" fill="none" stroke="#fff" stroke-width="1"><path d="M1 6 11 1l10 5v13H1z"/><path d="M1 6h20M6 9h10v10H6zM8 12h6M8 14h6M8 16h6"/></svg>
    PRODUCTION
  </div>
  <div class="tile">
    <svg width="22" height="20" viewBox="0 0 22 20" fill="none" stroke="#fff" stroke-width="1"><rect x="1" y="3" width="20" height="16"/><path d="M1 8h20M8 3v5M14 3v5"/><rect x="13" y="12" width="6" height="4" fill="#fff"/></svg>
    WAREHOUSING
  </div>
  <div class="tile">
    <svg width="26" height="20" viewBox="0 0 26 20" fill="none" stroke="#fff" stroke-width="1"><path d="M6 17h15a4.5 4.5 0 0 0 .5-9A7 7 0 0 0 8 7a5 5 0 0 0-2 10z"/><path d="m13 10 4 2-4 2-4-2zM9 12v4l4 2 4-2v-4M13 14v4"/></svg>
    KVT
  </div>
  <div class="tile">
    <svg width="24" height="22" viewBox="0 0 24 22" fill="none" stroke="#fff" stroke-width="1"><path d="M2 21h20M4 21v-3h6v3M14 21v-3h6v3M7 18V8l6-5 4 2M13 3v4M17 5v5"/><circle cx="7" cy="8" r="1.5"/><circle cx="13" cy="3" r="1.5"/></svg>
    AUTOMATION
  </div>
</nav>

<article class="abs card" style="left:207px;background:linear-gradient(135deg,#c9a56b 0%,#9fb2c9 55%,#7f8a99 100%)" role="img" aria-label="Man scanning boxes in a stockroom">
  <div class="card-caption">KVT<br>Development</div>
</article>
<article class="abs card" style="left:414px;background:linear-gradient(135deg,#3a4456 0%,#c49b6a 45%,#b58a5b 100%)" role="img" aria-label="Team checking parcels in a warehouse">
  <div class="card-caption">Warehouse<br>Management</div>
</article>
<article class="abs card" style="left:621px;background:linear-gradient(135deg,#8fa0b3 0%,#3b4d66 50%,#1e2b3d 100%)" role="img" aria-label="Worker at a bottling line">
  <div class="card-caption" style="left:17px">Automation<br>and Integration</div>
</article>

<h2 class="abs h2" style="left:213px;top:724px">Über uns</h2>
<p class="abs about-lead">Our top goal is clearly defined:<br>your satisfaction.</p>
<p class="abs about-body">We develop an optimal solution based on your specific internal logistics requirements. Our company will collaborate with you on the operational and technical requirements of your business and implement a software solution – either stand alone or integrated with your KVT® system.</p>
<a class="abs more" style="left:214px;top:869px"><i></i>Read Mroe</a>

<h2 class="abs h2" style="left:466px;top:724px">Our clients</h2>
<div class="abs clients">
  <div class="client"><b></b>Arvelo</div>
  <div class="client focus"><b></b>Corvane</div>
  <div class="client"><b></b>Brixhol</div>
  <div class="client"><b></b>Helmark</div>
  <div class="client"><b></b>Lumerin</div>
  <div class="client"><b></b>Solvik</div>
</div>
<a class="abs more" style="left:478px;top:869px"><i></i>Join in our family</a>

<section class="abs band"></section>
<p class="abs band-text">Join in our family happy clients</p>
<a class="abs btn-outline">CONTACT US</a>

<footer class="abs footer"></footer>
<div class="abs fcol" style="left:212px">
  <h4>Company</h4>
  <ul><li>About us</li><li>Services</li><li>Contact us</li><li>Career</li><li>Last News</li><li>Clients</li><li>FAQ</li></ul>
</div>
<div class="abs fcol" style="left:315px">
  <h4>Services</h4>
  <ul><li>KVT Development</li><li>Warehouse Management</li><li>Automation / Integration</li><li>Product number 4</li><li>Product number 5</li></ul>
</div>
<div class="abs fcol" style="left:447px">
  <h4>United States</h4>
  <p>VANTRIX -<br>Software Solutions For Logistics, Inc.<br>240 Harlow Ridge Ave., Suite 310<br>Fenwick, MI 48120<br><span class="mail">info@vantrix-lagerwerk.example</span><br>Tel: +1 555 014 2790<br>Fax: +1 555 014 2791</p>
</div>
<div class="abs fcol" style="left:607px">
  <h4>Germany</h4>
  <p>VANTRIX GmbH -<br>Softwareloesungen der Logistik<br>Lagerweg 14<br>61999 Mustertal<br><span class="mail">info@vantrix-lagerwerk.example</span><br>Tel: +49 6100 55500<br>Fax: +49 6100 555029</p>
</div>
<div class="abs social" style="left:760px;top:1042px" aria-label="Social links">
  <span style="background:#3b5a9a"></span><span style="background:#3fa6df"></span><span style="background:#d44132"></span>
</div>

<p class="abs legal" style="left:217px">Impring &nbsp;&nbsp; AGB</p>
<p class="abs legal" style="right:213px">© 2017 by VANTRIX GmbH / VANTRIX Inc.</p>

<a class="abs chat" aria-label="Chat">
  <svg width="22" height="19" viewBox="0 0 22 19"><path d="M2 1h18a1.5 1.5 0 0 1 1.5 1.5v10A1.5 1.5 0 0 1 20 14H9l-5 4v-4H2A1.5 1.5 0 0 1 .5 12.5v-10A1.5 1.5 0 0 1 2 1z" fill="#fff"/><circle cx="7" cy="7.5" r="1.2" fill="#cc0000"/><circle cx="11" cy="7.5" r="1.2" fill="#cc0000"/><circle cx="15" cy="7.5" r="1.2" fill="#cc0000"/></svg>
</a>

</body>
</html>
```